Ski and Snowboard Instructor Business card

An eye catching business card capturing the essence of the sport and the mountain with a professional finish and easily readable contact information.

Notes on uploaded files:
I must have the KORVE (Northern Guild of Alpine Coaching Standards) Logo featured on the design (I designed it on the front but you can move if you think it would look better else where). The front of the card as you will see is a picture of a mountain top, if you can find a real image of this with a clear blue sky and snow that would be great -even better if it was from New Zealand as that is where I will be using the card!!! but also I am open to creative ones - logo style, 2D mountain outline etc.
As for the back something clean and simple, I originally designed it as matt black background with stylised writing for my name and a contrasting colour for the other writing. Possibly add the tag line 'certified snowsports instructor' I didn't just because of spacing etc but I'm keen to see what you guys come up with.

Writing on the back
Jamie Whitcombe
SKI - SNOWBOARD
jamiewhitcombe2008@frostmail.example
NZ: 02107481639
UK: (+44) 07835519402
Hope this helps
Happy designing!

Industry/Entity Type

Business

Contact Information for Business Card

See description

Requirements
Must have
• KORVE (Northern guild of Alpine Coaching Standards) logo. It is a trademarked logo so please no alterations in shape or colour.
Nice to have
• Real Images of mountains, snow etc

```html
<!DOCTYPE html>
<html lang="en">
<head>
<meta charset="utf-8">
<title>Jamie Whitcombe – Snowsports Instructor Business Cards</title>
<link rel="stylesheet" href="https://fonts.googleapis.com/css2?family=Alegreya:ital,wght@1,400&family=Lato:wght@400;700&display=swap">
<style>
  :root {
    --backdrop: #474747;
    --card-black: #000000;
    --sky-top: #7f9fd3;
    --sky-low: #a9bfe0;
    --snow: #eef2f8;
    --rock: #8a94a6;
    --brand-blue: #1f6fb8;
    --brand-red: #e8493f;
    --white: #ffffff;
    --light-text: #e9e9e9;
  }
  * { box-sizing: border-box; margin: 0; padding: 0; }
  html, body { width: 1200px; height: 1000px; overflow: hidden; }
  body {
    background: var(--backdrop);
    position: relative;
    font-family: "Lato", Arial, sans-serif;
  }
  .card {
    position: absolute;
    width: 470px;
    height: 290px;
    overflow: hidden;
  }
  .card--front-a { left: 77px; top: 132px; }
  .card--back-a { left: 624px; top: 132px; }
  .card--front-b { left: 77px; top: 551px; }
  .card--back-b { left: 624px; top: 551px; }

  /* Front */
  .mountain-photo {
    position: absolute; inset: 0;
    background:
      linear-gradient(172deg, transparent 0 52%, var(--rock) 52.5%, var(--snow) 62%, #d6deea 80%, var(--snow) 100%),
      linear-gradient(180deg, var(--sky-top) 0%, var(--sky-low) 60%);
  }
  .brand {
    position: absolute;
    display: flex; align-items: center; gap: 6px;
    font-family: "Lato", Arial, sans-serif;
    font-weight: 700;
  }
  .brand__mark { width: 14px; height: 14px; background: currentColor; }
  .brand__name { letter-spacing: 1px; }
  .brand-sub {
    position: absolute;
    font-weight: 700;
    text-transform: uppercase;
    line-height: 1.15;
  }
  .card--front-a .brand, .card--front-b .brand { right: 28px; top: 30px; font-size: 26px; color: var(--white); }
  .card--front-a .brand-sub, .card--front-b .brand-sub { right: 28px; top: 62px; font-size: 6.5px; color: var(--white); text-align: right; width: 150px; }

  .front-name {
    position: absolute; left: 0; right: 0; top: 74px;
    text-align: center;
    font-family: "Alegreya", Georgia, serif;
    font-style: italic;
    font-size: 36px;
    letter-spacing: 0.5px;
  }
  .front-name--white { color: var(--white); }
  .front-name--blue { color: var(--brand-blue); }
  .front-role {
    position: absolute; left: 0; right: 0; top: 112px;
    text-align: center;
    color: var(--white);
    font-size: 12.5px;
  }

  /* Back */
  .card--back-a, .card--back-b { background: var(--card-black); }
  .card--back-a .brand, .card--back-b .brand { right: 28px; top: 30px; font-size: 38px; color: var(--brand-blue); }
  .card--back-a .brand-sub, .card--back-b .brand-sub { right: 28px; top: 76px; font-size: 9px; color: var(--brand-blue); width: 145px; }
  .back-name {
    position: absolute; left: 28px; top: 126px;
    font-family: "Alegreya", Georgia, serif;
    font-style: italic;
    font-size: 38px;
    letter-spacing: 0.5px;
  }
  .back-name--red { color: var(--brand-red); }
  .back-name--blue { color: var(--brand-blue); }
  .back-discipline {
    position: absolute; left: 29px; top: 168px;
    color: var(--light-text); font-size: 12.5px;
  }
  .contact-list {
    position: absolute; left: 30px; top: 206px;
    list-style: none;
    color: var(--light-text); font-size: 11px;
  }
  .contact-list li { display: flex; align-items: center; gap: 12px; height: 18px; }
  .contact-icon { width: 11px; height: 11px; flex: none; }
  .icons-blue { color: var(--brand-blue); }
  .icons-red { color: var(--brand-red); }
</style>
</head>
<body>

<!-- Front, white name -->
<section class="card card--front-a">
  <div class="mountain-photo" role="img" aria-label="Photograph of snow-covered mountain peaks under a clear blue sky"></div>
  <div class="brand"><span class="brand__mark"></span><span class="brand__name">KORVE</span></div>
  <p class="brand-sub">Northern Guild of Alpine Coaching Standards</p>
  <h1 class="front-name front-name--white">Jamie Whitcombe</h1>
  <p class="front-role">Certified Snowsports Instructor</p>
</section>

<!-- Back, red name -->
<section class="card card--back-a">
  <div class="brand"><span class="brand__mark"></span><span class="brand__name">KORVE</span></div>
  <p class="brand-sub">Northern Guild of Alpine Coaching Standards</p>
  <h2 class="back-name back-name--red">Jamie Whitcombe</h2>
  <p class="back-discipline">Ski - Snowboard</p>
  <ul class="contact-list icons-blue">
    <li><svg class="contact-icon" viewBox="0 0 12 12"><rect x="0.5" y="2" width="11" height="8" fill="currentColor"/><path d="M0.5 2 L6 6.5 L11.5 2" stroke="#000" stroke-width="1" fill="none"/></svg><span style="color:var(--light-text)">jamiewhitcombe2008@frostmail.example</span></li>
    <li><svg class="contact-icon" viewBox="0 0 12 12"><path d="M2 1 L4.5 1 L5 4 L3.5 5 Q4.5 7.5 7 8.5 L8 7 L11 7.5 L11 10 Q10 11.5 8 11 Q2 9 1 3 Q0.8 1.5 2 1 Z" fill="currentColor"/></svg><span style="color:var(--light-text)">NZ: 02107481639</span></li>
    <li><svg class="contact-icon" viewBox="0 0 12 12"><path d="M2 1 L4.5 1 L5 4 L3.5 5 Q4.5 7.5 7 8.5 L8 7 L11 7.5 L11 10 Q10 11.5 8 11 Q2 9 1 3 Q0.8 1.5 2 1 Z" fill="currentColor"/></svg><span style="color:var(--light-text)">UK: (+44) 07835519402</span></li>
  </ul>
</section>

<!-- Front, blue name -->
<section class="card card--front-b">
  <div class="mountain-photo" role="img" aria-label="Photograph of snow-covered mountain peaks under a clear blue sky"></div>
  <div class="brand"><span class="brand__mark"></span><span class="brand__name">KORVE</span></div>
  <p class="brand-sub">Northern Guild of Alpine Coaching Standards</p>
  <h2 class="front-name front-name--blue">Jamie Whitcombe</h2>
  <p class="front-role">Certified Snowsports Instructor</p>
</section>

<!-- Back, blue name -->
<section class="card card--back-b">
  <div class="brand"><span class="brand__mark"></span><span class="brand__name">KORVE</span></div>
  <p class="brand-sub">Northern Guild of Alpine Coaching Standards</p>
  <h2 class="back-name back-name--blue">Jamie Whitcombe</h2>
  <p class="back-discipline">Ski - Snowboard</p>
  <ul class="contact-list icons-red">
    <li><svg class="contact-icon" viewBox="0 0 12 12"><rect x="0.5" y="2" width="11" height="8" fill="currentColor"/><path d="M0.5 2 L6 6.5 L11.5 2" stroke="#000" stroke-width="1" fill="none"/></svg><span style="color:var(--light-text)">jamiewhitcombe2008@frostmail.example</span></li>
    <li><svg class="contact-icon" viewBox="0 0 12 12"><path d="M2 1 L4.5 1 L5 4 L3.5 5 Q4.5 7.5 7 8.5 L8 7 L11 7.5 L11 10 Q10 11.5 8 11 Q2 9 1 3 Q0.8 1.5 2 1 Z" fill="currentColor"/></svg><span style="color:var(--light-text)">NZ: 02107481639</span></li>
    <li><svg class="contact-icon" viewBox="0 0 12 12"><path d="M2 1 L4.5 1 L5 4 L3.5 5 Q4.5 7.5 7 8.5 L8 7 L11 7.5 L11 10 Q10 11.5 8 11 Q2 9 1 3 Q0.8 1.5 2 1 Z" fill="currentColor"/></svg><span style="color:var(--light-text)">UK: (+44) 07835519402</span></li>
  </ul>
</section>

</body>
</html>
```